Design a double sided business card

We are looking for a clean, eye-catching, and contemporary design that enhances the brand and presents a premium, professional image. Our preference is for a brown card with black gloss detailing and embossed elements; however, we are open to creative input and design suggestions that best achieve a strong visual impact.

Please see the attached existing business card for reference. We use both black and brown colours consistently across our branding.

On sample provided

```html
<!DOCTYPE html>
<html lang="en">
<head>
<meta charset="utf-8">
<title>Korvane business card</title>
<link rel="stylesheet" href="https://fonts.googleapis.com/css2?family=Montserrat:wght@400;500;700;800&display=swap">
<style>
  :root {
    --page: #b0b0b0;
    --card: #c8b49b;
    --ink: #111111;
    --emboss-dark: #9e8c76;
    --emboss-mid: #b9a68e;
    --emboss-light: #e6d9c8;
  }
  * { margin: 0; padding: 0; box-sizing: border-box; }
  html, body { width: 1081px; height: 1200px; overflow: hidden; background: var(--page); }
  body { font-family: "Montserrat", sans-serif; color: var(--ink); position: relative; }

  .card {
    position: absolute;
    left: 90px;
    width: 900px;
    height: 514px;
    border-radius: 40px;
    background: var(--card);
    overflow: hidden;
  }
  .card--front { top: 52px; }
  .card--back { top: 628px; }

  /* Front */
  .wordmark {
    position: absolute;
    left: 48px;
    top: 66px;
    font-weight: 800;
    font-size: 42px;
    letter-spacing: 0.09em;
    line-height: 1;
  }
  .holder { position: absolute; left: 48px; top: 178px; }
  .holder__name { font-weight: 700; font-size: 31px; line-height: 1; letter-spacing: -0.01em; }
  .holder__role { font-size: 19px; font-weight: 400; margin-top: 3px; }

  .address { position: absolute; left: 48px; top: 270px; font-size: 20px; line-height: 30px; font-weight: 500; }

  .contacts { position: absolute; left: 48px; top: 356px; list-style: none; font-size: 20px; font-weight: 500; }
  .contacts li { display: flex; align-items: center; height: 32px; }
  .contacts svg { width: 16px; height: 16px; margin-right: 10px; fill: var(--ink); flex: none; }

  .brand-block {
    position: absolute;
    left: 534px;
    top: 68px;
    width: 330px;
    height: 378px;
    background: var(--ink);
  }

  /* Back */
  .pattern-field {
    position: absolute; inset: 0;
    background: linear-gradient(90deg, var(--emboss-dark) 0%, var(--emboss-mid) 55%, var(--emboss-light) 100%);
  }
  .back-lockup {
    position: absolute;
    left: 0; right: 0;
    top: 208px;
    display: flex;
    flex-direction: column;
    align-items: center;
  }
  .back-lockup__panel {
    background: var(--card);
    padding: 18px 34px 14px;
    display: flex;
    flex-direction: column;
    align-items: center;
  }
  .back-lockup__row { display: flex; align-items: center; gap: 12px; }
  .back-lockup__square { width: 22px; height: 22px; background: var(--ink); }
  .back-lockup__name { font-weight: 800; font-size: 50px; letter-spacing: 0.09em; line-height: 1; }
  .back-lockup__url { font-weight: 500; font-size: 19px; letter-spacing: 0.2em; margin-top: 10px; }
</style>
</head>
<body>

<section class="card card--front" aria-label="Business card front">
  <div class="wordmark">KORVANE</div>

  <div class="holder">
    <div class="holder__name">DANA MERCER</div>
    <div class="holder__role">Director</div>
  </div>

  <div class="address">
    12 Millbrook Yard<br>
    Eastford EF4 2LR
  </div>

  <ul class="contacts">
    <li>
      <svg viewBox="0 0 16 16" aria-hidden="true"><path d="M3.5 1.5l2.3 2.8-1.3 1.6c.9 2 2.6 3.7 4.6 4.6l1.6-1.3 2.8 2.3-1.2 2.2C7.4 14.9 1.1 8.6.9 3.9z"/></svg>
      0800 555 0142
    </li>
    <li>
      <svg viewBox="0 0 16 16" aria-hidden="true"><path d="M4.5 0h7A1.5 1.5 0 0 1 13 1.5v13a1.5 1.5 0 0 1-1.5 1.5h-7A1.5 1.5 0 0 1 3 14.5v-13A1.5 1.5 0 0 1 4.5 0zm.3 2v10.5h6.4V2zM8 13.3a.9.9 0 1 0 0 1.8.9.9 0 0 0 0-1.8z"/></svg>
      07700900461
    </li>
    <li>
      <svg viewBox="0 0 16 16" aria-hidden="true"><path d="M1 3.5h14v9H1zm1.3 1.2L8 9l5.7-4.3z"/></svg>
      dana@korvane.co.uk
    </li>
    <li>
      <svg viewBox="0 0 16 16" aria-hidden="true"><path d="M8 1a7 7 0 1 0 0 14A7 7 0 0 0 8 1zm0 1.3c.7.7 1.3 2 1.5 3.5h-3C6.7 4.3 7.3 3 8 2.3zM2.4 7.2h3a11 11 0 0 0 0 1.6h-3a5.6 5.6 0 0 1 0-1.6zm4.1 0h3a9 9 0 0 1 0 1.6h-3a9 9 0 0 1 0-1.6zm4.1 0h3a5.6 5.6 0 0 1 0 1.6h-3a11 11 0 0 0 0-1.6zM6.5 10.2h3C9.3 11.7 8.7 13 8 13.7c-.7-.7-1.3-2-1.5-3.5z"/></svg>
      www.korvane.co.uk
    </li>
  </ul>

  <div class="brand-block" aria-hidden="true"></div>
</section>

<section class="card card--back" aria-label="Business card back">
  <div class="pattern-field" role="img" aria-label="Embossed repeating brand pattern in tan tones, darker on the left fading lighter to the right"></div>
  <div class="back-lockup">
    <div class="back-lockup__panel">
      <div class="back-lockup__row">
        <span class="back-lockup__square" aria-hidden="true"></span>
        <span class="back-lockup__name">KORVANE</span>
      </div>
      <div class="back-lockup__url">WWW.KORVANE.CO.UK</div>
    </div>
  </div>
</section>

</body>
</html>
```